Business Card Design

wig manufacturer
I would like something very upscale.highend looking
maybe mat chrome card with shiney chrome
or something like the Quorix business card very clean and simple white with the logo in silver
Target Market(s)
upscale women
Industry/Entity Type
Business
Contact Information for Business Card
OUR LOGO
company name:Marisol Tresses
48E52Street Dennis Holcroft
New York,N.Y 10022
Tel:646-5817730
1800-4369185
email:hairloft@zentrimail.com
website:Marisoltresses.com
Look and feel
Each slider illustrates characteristics of the customer's brand and the style your logo design should communicate.

```html
<!DOCTYPE html>
<html lang="en">
<head>
<meta charset="utf-8">
<title>Marisol Tresses – Business Card</title>
<link href="https://fonts.googleapis.com/css2?family=Arimo:wght@400;700&display=swap" rel="stylesheet">
<style>
  :root {
    --backdrop: #f4f4f4;
    --chrome-light: #c9c9c9;
    --chrome-mid: #a9a9a9;
    --chrome-dark: #8c8c8c;
    --ink-white: #ffffff;
    --brand-ink: #7a7a7a;
    --divider: rgba(255,255,255,0.85);
  }
  * { margin: 0; padding: 0; box-sizing: border-box; }
  html, body {
    width: 1200px; height: 900px; overflow: hidden;
    background: var(--backdrop);
    font-family: "Arimo", Arial, sans-serif;
  }
  .stage {
    width: 1200px; height: 900px;
    display: flex; align-items: center; justify-content: center;
  }
  .card {
    position: relative;
    width: 900px; height: 510px;
    background: linear-gradient(180deg,
      var(--chrome-mid) 0%,
      var(--chrome-light) 30%,
      var(--chrome-mid) 55%,
      var(--chrome-dark) 80%,
      var(--chrome-mid) 100%);
    box-shadow: 0 18px 40px rgba(0,0,0,0.18);
  }
  .brand {
    position: absolute;
    left: 0; top: 0; width: 510px; height: 100%;
    display: flex; align-items: center; justify-content: center; gap: 16px;
  }
  .brand-dot {
    width: 22px; height: 22px; border-radius: 50%;
    background: var(--brand-ink);
  }
  .brand-name {
    font-size: 44px; font-weight: 400; color: var(--brand-ink);
    letter-spacing: 1px; white-space: nowrap;
  }
  .divider {
    position: absolute; left: 510px; top: 110px;
    width: 1.5px; height: 380px; background: var(--divider);
  }
  .contact {
    position: absolute; left: 542px; top: 105px;
    color: var(--ink-white);
  }
  .contact-name {
    font-size: 27px; font-weight: 700; margin-bottom: 26px;
  }
  .contact-group { margin-bottom: 26px; }
  .contact-line {
    display: flex; align-items: flex-start; gap: 8px;
    font-size: 25px; line-height: 34px; white-space: nowrap;
  }
  .contact-line svg {
    width: 22px; height: 22px; flex: none; margin-top: 7px;
    fill: var(--ink-white);
  }
</style>
</head>
<body>
<main class="stage">
  <section class="card">
    <div class="brand">
      <span class="brand-dot"></span>
      <span class="brand-name">Marisol Tresses</span>
    </div>

    <div class="divider"></div>

    <div class="contact">
      <p class="contact-name">Dennis Holcroft</p>

      <div class="contact-group">
        <p class="contact-line">
          <svg viewBox="0 0 24 24" aria-hidden="true"><path d="M6.6 10.8a15 15 0 0 0 6.6 6.6l2.2-2.2c.3-.3.7-.4 1-.2 1.1.4 2.3.6 3.6.6.6 0 1 .4 1 1V20c0 .6-.4 1-1 1A17 17 0 0 1 3 4c0-.6.4-1 1-1h3.5c.6 0 1 .4 1 1 0 1.3.2 2.5.6 3.6.1.3 0 .7-.2 1z"/></svg>
          646-5817730
        </p>
        <p class="contact-line">
          <svg viewBox="0 0 24 24" aria-hidden="true"><path d="M6.6 10.8a15 15 0 0 0 6.6 6.6l2.2-2.2c.3-.3.7-.4 1-.2 1.1.4 2.3.6 3.6.6.6 0 1 .4 1 1V20c0 .6-.4 1-1 1A17 17 0 0 1 3 4c0-.6.4-1 1-1h3.5c.6 0 1 .4 1 1 0 1.3.2 2.5.6 3.6.1.3 0 .7-.2 1z"/></svg>
          1800-4369185
        </p>
        <p class="contact-line">
          <svg viewBox="0 0 24 24" aria-hidden="true"><path d="M7 2h10v5H7zM4 8h16a2 2 0 0 1 2 2v6h-4v6H6v-6H2v-6a2 2 0 0 1 2-2zm4 8v4h8v-4z"/></svg>
          646-5817741
        </p>
      </div>

      <div class="contact-group">
        <p class="contact-line">
          <svg viewBox="0 0 24 24" aria-hidden="true"><path d="M2 6h20v12H2zm2 1.5V8l8 5 8-5v-.5z"/></svg>
          hairloft@zentrimail.com
        </p>
        <p class="contact-line">
          <svg viewBox="0 0 24 24" aria-hidden="true"><path d="M12 2a10 10 0 1 0 0 20 10 10 0 0 0 0-20zm6.9 6h-3a15 15 0 0 0-1.3-4A8 8 0 0 1 18.9 8zM12 4c.8 1.2 1.5 2.5 1.9 4h-3.8c.4-1.5 1.1-2.8 1.9-4zM4.3 14a8 8 0 0 1 0-4h3.4a16 16 0 0 0 0 4zm.8 2h3a15 15 0 0 0 1.3 4A8 8 0 0 1 5.1 16zm3-8h-3a8 8 0 0 1 4.3-4A15 15 0 0 0 8.1 8zM12 20c-.8-1.2-1.5-2.5-1.9-4h3.8c-.4 1.5-1.1 2.8-1.9 4zm2.3-6H9.7a14 14 0 0 1 0-4h4.6a14 14 0 0 1 0 4zm.3 6a15 15 0 0 0 1.3-4h3a8 8 0 0 1-4.3 4zm1.7-6a16 16 0 0 0 0-4h3.4a8 8 0 0 1 0 4z"/></svg>
          Marisoltresses.com
        </p>
      </div>

      <div class="contact-group">
        <p class="contact-line">
          <svg viewBox="0 0 24 24" aria-hidden="true"><path d="M12 3 1 12h3v9h6v-6h4v6h6v-9h3z"/></svg>
          <span>48E52Street<br>New York,N.Y 10022</span>
        </p>
      </div>
    </div>
  </section>
</main>
</body>
</html>
```